I need to redesign this website. Modern Fun Professional Redesign For www.JollyPerkHub.com = New Name www.ClaimVouchly.com

Use existing content as it is on website exactly and we will revise after initial mock ups.

The new name will be ClaimVouchly.com please make a quick logo for this site too while redesigning.

Make it look like an official website....

Target Market(s)

Consumers that are redeeming certificates that businesses gave to them as a gift for customer loyalty,e tc.

Industry/Entity Type

It Professional

Logo Text

www.ClaimVouchly.com

Number of Pages Required

4 page

Colors

Designer to choose colors to be used in the design.

Requirements
Must have
• Must look professional, build trust and credibility.
Nice to have
• open
Should not have
• open

```html
<!DOCTYPE html>
<html lang="en">
<head>
<meta charset="utf-8">
<title>Claim Vouchly – Redemption Process Center</title>
<link rel="stylesheet" href="https://fonts.googleapis.com/css2?family=Raleway:wght@400;500;600&family=Lato:ital,wght@0,400;1,400&display=swap">
<style>
:root{
  --green:#3fb78f;
  --green-text:#34b183;
  --page:#f5f6f8;
  --ink:#222;
  --grey:#5b5b5b;
  --navy:#1f2a55;
  --orange:#f39a1b;
  --orange-text:#e8841a;
  --panel:rgba(28,42,56,.86);
  --white:#fff;
}
*{box-sizing:border-box;margin:0;padding:0}
html,body{width:1200px;height:1138px;overflow:hidden;background:var(--page)}
body{position:relative;font-family:"Raleway",sans-serif;color:var(--ink)}

.site-header{position:absolute;left:0;top:0;width:1200px;height:106px;background:var(--page)}
.brand{position:absolute;left:165px;top:46px;display:flex;align-items:center;gap:10px;font-size:31px;font-weight:500;color:var(--green)}
.brand-dot{width:16px;height:16px;border-radius:50%;background:var(--green)}
.main-nav{position:absolute;top:70px;left:672px;display:flex;gap:37px;font-size:16px;font-weight:500}
.main-nav a{color:var(--ink);text-decoration:none}
.main-nav a.is-active{color:var(--green)}

.hero{position:absolute;left:0;top:106px;width:1200px;height:375px;background:linear-gradient(180deg,#5e9ec9 0%,#7fb6d9 55%,#a9d1ea 100%)}
.hero-panel{position:absolute;left:187px;top:60px;width:826px;height:262px;background:var(--panel);border-radius:8px;text-align:center;color:var(--white)}
.hero-title{margin-top:22px;font-size:36px;font-weight:500;line-height:1.2}
.hero-title span{color:var(--orange-text)}
.hero-sub{margin-top:8px;font-size:17px;font-weight:500}
.hero-copy{margin-top:14px;font-size:17px;font-weight:500;line-height:27px}
.cert-form{position:absolute;left:282px;top:169px;width:262px;height:48px;border:1px solid rgba(255,255,255,.45);border-radius:4px;display:flex}
.cert-input{flex:1;padding-left:12px;display:flex;align-items:center;font-family:"Lato",sans-serif;font-style:italic;font-size:14px}
.cert-go{width:57px;height:100%;background:var(--orange);border-radius:0 4px 4px 0;font-family:"Lato",sans-serif;font-size:25px;display:flex;align-items:center;justify-content:center}

.about{position:absolute;left:0;top:540px;width:1200px;text-align:center;font-size:19.5px;font-weight:500;color:var(--grey)}
.about p{position:absolute;left:0;width:1200px}
.about .quote{color:var(--green-text)}
.about a{color:var(--green-text);text-decoration:underline;text-underline-offset:4px}

.reviews-title{position:absolute;left:0;top:808px;width:1200px;text-align:center;font-family:"Lato",sans-serif;font-style:italic;font-weight:400;font-size:35px;color:var(--green)}
.review{position:absolute;top:911px;width:413px;height:108px;background:var(--white);font-family:"Lato",sans-serif}
.review-photo{position:absolute;left:24px;top:-24px;width:78px;height:72px;background:var(--page);padding:3px 7px}
.review-photo div{width:100%;height:100%;background:linear-gradient(160deg,#9aa3a8,#4e575c)}
.review-name{position:absolute;left:118px;top:8px;font-size:12.5px;color:var(--navy)}
.review-date{position:absolute;left:118px;top:28px;font-size:12.5px;color:var(--orange)}
.review-mark{position:absolute;right:10px;top:6px;font-family:Georgia,serif;font-size:30px;line-height:1;color:#a7dcc8}
.review-text{position:absolute;left:21px;top:60px;width:392px;font-size:11px;line-height:21px;white-space:nowrap;color:var(--ink)}
.more-link{position:absolute;left:0;top:1041px;width:1176px;text-align:center;font-family:"Lato",sans-serif;font-style:italic;font-size:14px}
.more-link a{color:var(--navy)}

.site-footer{position:absolute;left:0;top:1098px;width:1200px;height:40px;background:var(--green);color:var(--white);font-family:"Lato",sans-serif;font-style:italic;font-size:12px}
.site-footer .copy{position:absolute;left:163px;top:12px}
.site-footer .id{position:absolute;right:162px;top:13px}
</style>
</head>
<body>
<header class="site-header">
  <div class="brand"><span class="brand-dot"></span>Claim Vouchly</div>
  <nav class="main-nav">
    <a class="is-active" href="#">Home</a>
    <a href="#">Contact Us</a>
    <a href="#">Testimonials</a>
    <a href="#">Terms</a>
  </nav>
</header>

<section class="hero" role="img" aria-label="Photo of a passenger jet flying overhead against a blue sky">
  <div class="hero-panel">
    <h1 class="hero-title">Welcome To <span>The Voucher Desk</span></h1>
    <p class="hero-sub">Redemption Process Center</p>
    <p class="hero-copy">Please Enter A Valid Certificate Id In The Form Below<br>To Redeem Your Certificate And To View Faq’s, Terms And Locations.</p>
    <div class="cert-form">
      <div class="cert-input">Certificate Id</div>
      <div class="cert-go">Go</div>
    </div>
  </div>
</section>

<section class="about">
  <p style="top:0">ClaimVouchly.com is a leading company in travel certificate fulfillment.</p>
  <p style="top:44px">Our goal is to make it easy for you to redeem your certificate and our philosophy is this:</p>
  <p class="quote" style="top:88px">“What good is it to receive a gift certificate if you can’t use it?”.</p>
  <p style="top:126px">If you have any questions about how to redeem a certain certificate, please contact us.</p>
  <p style="top:162px"><a href="#">We are here to help.</a></p>
</section>

<h2 class="reviews-title">Happy Customer Reviews</h2>

<article class="review" style="left:161px">
  <div class="review-photo"><div role="img" aria-label="Customer portrait photo"></div></div>
  <div class="review-name">Nora P.&nbsp; - &nbsp;Athens, GA</div>
  <div class="review-date">Added on 06/23/2017 06:24:16 pm</div>
  <div class="review-mark">”</div>
  <p class="review-text">Paige was a “saving grace.’ She followed up and helped me book the vacation<br>and air fare. Paige was positive and did everything she promised to do.</p>
</article>

<article class="review" style="left:626px">
  <div class="review-photo"><div role="img" aria-label="Customer portrait photo"></div></div>
  <div class="review-name">Jo Ellen T. - Mesa, AZ</div>
  <div class="review-date">Added on 05/31/2017 04:27:10 pm</div>
  <div class="review-mark">”</div>
  <p class="review-text">Declan was able to put together our flight schedule. He was very patient with<br>us &amp; diligent in working out all the changes I was requesting. Thank you, Dec.</p>
</article>

<p class="more-link"><a href="#">Click here to view more testimonials</a></p>

<footer class="site-footer">
  <span class="copy">Copyright ©2017&nbsp; Claim Vouchly.&nbsp; All Rights Reserved.</span>
  <span class="id">Travel ID # CST 4817306</span>
</footer>
</body>
</html>
```